Software company specialized in data analytics and professional services

We need a landing page design for our business. It should include our logo design. It should have multiple sections :
- stylish head
- what we do (data analytics software, professional services)
- contact form

Target Market(s)

Companies, B2B

Industry/Entity Type

Data

Number of Pages Required

1 page

Font styles to use
Sans Serif

Requirements
Must have
• Dark theme
Should not have
• Gradients on buttons

```html
<!DOCTYPE html>
<html lang="en">
<head>
<meta charset="UTF-8">
<title>Veltrix — Empowering Growth</title>
<link href="https://fonts.googleapis.com/css2?family=Arimo:wght@400;700&display=swap" rel="stylesheet">
<style>
  :root {
    --bg: #020304;
    --teal: #0f6f66;
    --teal-deep: #0a3f3b;
    --maroon: #5c2430;
    --text: #ffffff;
    --brand: #8a3fd0;
    --button-bg: #ffffff;
    --button-text: #111111;
  }
  * { margin: 0; padding: 0; box-sizing: border-box; }
  html, body {
    width: 1200px;
    height: 606px;
    overflow: hidden;
    background: var(--bg);
    font-family: "Arimo", Arial, sans-serif;
    color: var(--text);
  }
  .hero {
    position: relative;
    width: 1200px;
    height: 606px;
    overflow: hidden;
    background:
      radial-gradient(ellipse 520px 420px at 1080px 230px, var(--teal) 0%, var(--teal-deep) 45%, rgba(2,3,4,0) 100%),
      radial-gradient(ellipse 420px 300px at 110px 600px, var(--maroon) 0%, rgba(92,36,48,0.45) 45%, rgba(2,3,4,0) 100%),
      var(--bg);
  }
  .site-header {
    position: absolute;
    top: 26px;
    left: 86px;
    right: 66px;
    display: flex;
    align-items: center;
    justify-content: space-between;
  }
  .brand-name {
    font-weight: 700;
    font-size: 19px;
    letter-spacing: 1px;
    color: var(--brand);
  }
  .main-nav {
    display: flex;
    gap: 0;
  }
  .main-nav a {
    color: var(--text);
    text-decoration: none;
    font-size: 14px;
  }
  .main-nav .nav-about { margin-right: 78px; }
  .main-nav .nav-services { margin-right: 82px; }
  .hero-content {
    position: absolute;
    top: 138px;
    left: 0;
    width: 100%;
    text-align: center;
  }
  .hero-title {
    font-weight: 400;
    font-size: 84px;
    line-height: 86px;
    letter-spacing: 1px;
  }
  .hero-text {
    width: 590px;
    margin: 80px auto 0;
    font-size: 17px;
    line-height: 20px;
  }
  .cta-button {
    display: inline-block;
    margin-top: 46px;
    width: 154px;
    height: 33px;
    line-height: 33px;
    border-radius: 17px;
    background: var(--button-bg);
    color: var(--button-text);
    font-size: 15px;
    text-decoration: none;
  }
</style>
</head>
<body>
  <section class="hero">
    <header class="site-header">
      <div class="brand-name">VELTRIX</div>
      <nav class="main-nav">
        <a class="nav-about" href="#about">About</a>
        <a class="nav-services" href="#services">Services</a>
        <a class="nav-contact" href="#contact">Contact</a>
      </nav>
    </header>
    <div class="hero-content">
      <h1 class="hero-title">EMPOWERING<br>GROWTH</h1>
      <p class="hero-text">Lorem ipsum, dolor sit amet consectetur adipisicing elit. Quisquam distinctio provident quasi expedita sit a aspernatur unde est suscipit? Neque molestias porro veniam nisi?</p>
      <a class="cta-button" href="#contact">Get in Touch</a>
    </div>
  </section>
</body>
</html>
```